Kettle Book Cover

I am in need of cover design for a book/ebook. The title is Kettle. My name is my brand so Calvin Hosking should be obvious at thumb nail size. Addition verbage in small print: Author of The Lantern Tide
The cover art should be relatively simple. I'm looking for a skinny girl(preferably blonde) dressed in worn out, raggedy clothes. I would like one her hands to be covering her eyes as if hiding them, though if at all possible I would like a red eye to be seen through a gap in her fingers. Not a glowing eye, but red none the less(and no whites)
I would be interested to see black and white versions, muted color versions and full color versions.
The back cover will have the following blurb:
Twelve-year-old Nellie Brock bears the unfortunate nickname "Odd." A name even her bar hopping, alcoholic mother uses—that is when she's sober enough even to recognize the girl. Odd doesn't protest. This is her life and it can be no other way, not when she's deformed as she is.
Born with a combination of rare birth defects, Odd's eyes are a startling and dreadful red. Demon eyes is the first thought that springs to mind and the little girl takes care to hide them behind dark sunglasses. This is something her mother insists on, except when she's trading freak show peaks for dollars or drinks. A practice that is a nightly torture for the girl.
Yet when her mom abandons her, Odd discovers that loneliness and fear of the unknown are far worse than being a freak. Desperate for the least love, the girl with red eyes begins a quest through the American underclass that takes her halfway across the country. She thinks she's in search of her mother, but in truth she's looking for so much more.

Target Market(s)

Females ages 14-64

Industry/Entity Type

Nail

Requirements
Must have
• The cover art should be relatively simple. I'm looking for a skinny girl(preferably blonde) dressed in worn out, raggedy clothes. I would like one her hands to be covering her eyes as if hiding them, though if at all possible I would like a red eye to be seen through a gap in her fingers. Not a glowing eye, but red none the less(and no whites)
Should not have
• The girl can't look like a monster in any way. Sympathy is what I'm looking for.

```html
<!DOCTYPE html>
<html lang="en">
<head>
<meta charset="utf-8">
<title>Kettle — Calvin Hosking</title>
<link rel="stylesheet" href="https://fonts.googleapis.com/css2?family=Marcellus&family=Tinos&display=swap">
<style>
  :root {
    --page: #ffffff;
    --ink-dark: #0d0d10;
    --road: #3a3a40;
    --road-light: #55555d;
    --sky-light: #e4e6ee;
    --sky-mid: #aeb2c2;
    --tree: #141417;
    --title-red: #c8141c;
    --text-white: #f4f4f4;
    --skin-light: #d6a894;
    --skin: #b98672;
    --skin-shadow: #7d5646;
    --hair: #a88a62;
    --hair-dark: #6e5a44;
  }
  * { margin: 0; padding: 0; box-sizing: border-box; }
  html, body { width: 1200px; height: 891px; overflow: hidden; background: var(--page); }
  .canvas { position: relative; width: 1200px; height: 891px; }

  .book-jacket {
    position: absolute; left: 85px; top: 95px;
    width: 1030px; height: 700px;
    display: flex;
  }

  /* Back cover */
  .back-cover {
    position: relative; width: 460px; height: 100%;
    overflow: hidden;
  }
  .back-cover .scene-art {
    position: absolute; inset: 0;
    background:
      linear-gradient(115deg, rgba(0,0,0,0) 0 40%, rgba(90,90,98,.55) 58%, rgba(0,0,0,0) 80%),
      linear-gradient(180deg, var(--sky-light) 0%, var(--sky-mid) 20%, #6a6c78 27%, var(--tree) 31%, var(--ink-dark) 36%, #1c1c22 55%, var(--road) 100%);
  }
  .blurb {
    position: absolute; left: 26px; right: 30px; top: 250px;
    font-family: "Tinos", "Times New Roman", serif;
    font-size: 15px; line-height: 1.26;
    color: var(--text-white);
    text-shadow: 0 1px 2px rgba(0,0,0,.6);
  }
  .blurb p + p { margin-top: 14px; }

  /* Spine */
  .spine {
    position: relative; width: 90px; height: 100%;
    background: linear-gradient(180deg, #16161a 0%, var(--ink-dark) 60%, #1d1d24 100%);
  }
  .spine-author, .spine-title {
    position: absolute; left: 50%;
    white-space: nowrap;
    font-family: "Marcellus", "Times New Roman", serif;
  }
  .spine-author {
    top: 130px; font-size: 34px; color: var(--text-white); letter-spacing: 3px;
    transform: translate(-50%, -50%) rotate(-90deg);
  }
  .spine-title {
    top: 560px; font-size: 54px; color: var(--title-red); letter-spacing: 5px;
    transform: translate(-50%, -50%) rotate(-90deg);
  }

  /* Front cover */
  .front-cover {
    position: relative; width: 480px; height: 100%;
    overflow: hidden;
  }
  .front-cover .scene-art {
    position: absolute; inset: 0;
    background:
      linear-gradient(180deg, rgba(0,0,0,0) 0 72%, rgba(20,16,14,.55) 100%),
      radial-gradient(ellipse 34% 44% at 74% 60%, var(--skin-light) 0%, var(--skin) 45%, rgba(125,86,70,0) 80%),
      radial-gradient(ellipse 22% 30% at 52% 80%, rgba(185,134,114,.85) 0%, rgba(125,86,70,0) 75%),
      radial-gradient(ellipse 45% 38% at 82% 18%, var(--hair) 0%, rgba(110,90,68,0) 72%),
      linear-gradient(90deg, rgba(0,0,0,0) 0 44%, rgba(125,86,70,.75) 60%, var(--skin-shadow) 80%, var(--hair-dark) 100%),
      linear-gradient(100deg, rgba(0,0,0,0) 0 8%, rgba(95,95,104,.7) 22%, rgba(0,0,0,0) 40%),
      linear-gradient(180deg, var(--sky-light) 0%, #c4c7d2 12%, var(--tree) 26%, #1e1e24 40%, var(--road-light) 70%, var(--road) 100%);
  }
  .front-title {
    position: absolute; left: 70px; top: 24px;
    font-family: "Marcellus", "Times New Roman", serif;
    font-size: 118px; line-height: 1; letter-spacing: 8px; font-weight: 400;
    color: var(--title-red);
    text-shadow: 0 2px 3px rgba(0,0,0,.45);
  }
  .front-author {
    position: absolute; left: 0; right: 0; bottom: 70px;
    text-align: center;
    font-family: "Marcellus", "Times New Roman", serif;
    font-size: 44px; letter-spacing: 5px;
    color: var(--text-white);
    text-shadow: 0 1px 3px rgba(0,0,0,.6);
  }
  .front-credit {
    position: absolute; left: 0; right: 0; bottom: 38px;
    text-align: center;
    font-family: "Tinos", "Times New Roman", serif;
    font-size: 21px;
    color: var(--text-white);
    text-shadow: 0 1px 3px rgba(0,0,0,.6);
  }
</style>
</head>
<body>
<div class="canvas">
  <div class="book-jacket">

    <section class="back-cover">
      <div class="scene-art" role="img" aria-label="Photograph of an empty two-lane country road at dusk, lined by dark silhouetted trees under a pale grey sky"></div>
      <div class="blurb">
        <p>Twelve-year-old Nellie Brock bears the unfortunate nickname “Odd.” A name even her bar hopping, alcoholic mother uses—that is when she’s sober enough even to recognize the girl. Odd doesn’t protest. This is her life and it can be no other way, not when she’s deformed as she is.</p>
        <p>Born with a combination of rare birth defects, Odd’s eyes are a startling and dreadful red. Demon eyes is the first thought that springs to mind and the little girl takes care to hide them behind dark sunglasses. This is something her mother insists on, except when she’s trading freak show peaks for dollars or drinks. A practice that is a nightly torture for the girl. Yet when her mom abandons her, Odd discovers that loneliness and fear of the unknown are far worse than being a freak. Desperate for the least love, the girl with red eyes begins a quest through the American underclass that takes her halfway across the country. She thinks she’s in search of her mother, but in truth she’s looking for so much more.</p>
      </div>
    </section>

    <section class="spine">
      <span class="spine-author">Hosking</span>
      <span class="spine-title">Kettle</span>
    </section>

    <section class="front-cover">
      <div class="scene-art" role="img" aria-label="Photograph of a blonde girl with red eyes resting her chin on her hand, set over a country road with a treeline fading into the distance"></div>
      <h1 class="front-title">Kettle</h1>
      <p class="front-author">Calvin Hosking</p>
      <p class="front-credit">The Author of The Lantern Tide</p>
    </section>

  </div>
</div>
</body>
</html>
```